Survey App for phone users trying a new phone with Dual connectivity

Survey App Brief<br/>Design For an Android Survey App for users' feedback on Call, SMS, Data and Streaming Experience on their Mobile phones.<br/><br/>Purpose of the App<br/>To ensure that the user's experience is not impacted by the network switching between two network on the special mobile phones they newly started using.<br/><br/>App Requirements:<br/>First screen: The registration screen, where the user needs to enter the following:<br/>Name: text box<br/>Phone Number: text box<br/>Group Number : <br/><br/>An information text:<br/>By Registering I agree to participate in the Survey.<br/><br/>Register: Button<br/><br/>Start Screen - Survey screens (next time user open the App this will be the first screen):<br/>We need feedback for 4 indicators:<br/>Call Experience<br/>SMS Experience<br/>Data Experience<br/>Streaming Experience<br/><br/>Each Experience can be in the form of a questionnaire or Satisfied/ Somewhat Satisfied / Extremely Satisfied form with radio buttons or on a scale of 1 to 5. We need to ensure that the format used is very professional.<br/><br/>An optional text box for the user to enter the comment in a free format.<br/><br/>This can be done in 4 different screens or in one single screen if it does not give a clumsy look.<br/><br/>A Send button at the end to submit the Survey.<br/><br/>We need a burger menu at the top left corner of this screen, which when expanded will provide 5 options:<br/>Edit User Profile<br/>Survey interval Timer<br/>FAQ<br/>Exit<br/>About<br/><br/><br/>Please ensure that the app is simple, friendly, lively and professional at the same time so that it ignites an interest in the user to use the app.<br/>Use Logo as appropriate.
Industry/Entity Type
Telecommunications
Colors
Designer to choose colors to be used in the design.
Look and feel
Each slider illustrates characteristics of the customer's brand and the style your logo design should communicate.

```html
<!DOCTYPE html>
<html lang="en">
<head>
<meta charset="utf-8">
<title>Survey App – Model 2</title>
<link rel="stylesheet" href="https://fonts.googleapis.com/css2?family=Roboto:wght@400;500;700&display=swap">
<style>
:root{
  --bg:#d0d0d0;
  --brand:#4fb0f2;
  --brand-light:#c9ebfd;
  --field:#87d4f5;
  --navy:#0d4aa8;
  --ink:#1a1a1a;
  --muted:#555;
  --back:#5a5a5a;
  --comment:#eeeeee;
  --white:#ffffff;
  --dim:#818181;
  --dim-panel:#3c5f7e;
}
*{box-sizing:border-box;margin:0;padding:0}
html,body{width:1099px;height:1200px;overflow:hidden;background:var(--bg);font-family:'Roboto',sans-serif}
.stage{position:absolute;left:0;top:0;width:1846px;height:2016px;transform:scale(0.5953);transform-origin:0 0}
.page-title{position:absolute;left:0;width:100%;top:88px;text-align:center;font-size:62px;font-weight:700;color:var(--navy);letter-spacing:1px;padding-left:50px}
.screen-label{position:absolute;font-size:37px;color:var(--ink);text-align:center;width:460px;top:255px;letter-spacing:.5px}
.screen-label.lower{top:1128px}
.screen{position:absolute;width:376px;height:668px;overflow:hidden;background:var(--white)}
.status{position:absolute;left:0;top:0;width:100%;height:30px;color:var(--white);font-size:16px;font-weight:500}
.status .time{position:absolute;left:9px;top:6px}
.status svg{position:absolute;right:6px;top:4px}
/* splash */
.splash{background:var(--brand)}
.splash-brand{position:absolute;left:0;width:100%;top:282px;display:flex;align-items:center;justify-content:center;gap:14px;color:var(--white);font-size:21px;font-weight:500;letter-spacing:2px}
.splash-brand .dot{width:46px;height:46px;border-radius:50%;background:var(--white)}
/* shared header + card */
.header{position:absolute;left:0;top:0;width:100%;height:170px;background:var(--brand)}
.card{position:absolute;left:0;top:108px;width:100%;bottom:0;background:var(--white);border-radius:50px 50px 0 0}
.reg-title{position:absolute;top:38px;width:100%;text-align:center;color:var(--white);font-size:30px;font-weight:500}
.field{position:absolute;left:38px;width:300px;height:50px;background:var(--field);border-radius:8px;font-size:18px;color:#222;padding:14px 0 0 14px}
.agree{position:absolute;top:521px;width:100%;text-align:center;font-size:13px;color:#444}
.btn-register{position:absolute;left:98px;top:566px;width:180px;height:50px;background:var(--brand);border-radius:6px;color:var(--white);font-size:30px;font-weight:500;text-align:center;line-height:50px}
/* survey */
.burger{position:absolute;left:17px;top:58px}
.survey-title{position:absolute;left:86px;top:56px;color:var(--white);font-size:31px;font-weight:500}
.feedback{position:absolute;top:124px;width:100%;text-align:center;color:var(--brand);font-size:27px}
.question{position:absolute;left:15px;top:165px;width:346px;height:300px;border-radius:10px;background:linear-gradient(180deg,var(--brand-light),var(--brand))}
.question h2{position:absolute;left:26px;top:18px;font-size:27px;font-weight:500;color:var(--ink)}
.option{position:absolute;left:25px;width:301px;height:48px;background:var(--white);border-radius:10px;box-shadow:0 3px 5px rgba(0,0,0,.18);font-size:19px;color:var(--muted);padding:12px 0 0 65px}
.option::before{content:"";position:absolute;left:21px;top:13px;width:22px;height:22px;border-radius:50%;border:2px solid var(--brand);background:var(--white)}
.option.selected{color:var(--navy);font-weight:500}
.option.selected::before{background:var(--navy);border-color:#8fc8f0}
.opt-1{top:66px}.opt-2{top:140px}.opt-3{top:213px}
.comments{position:absolute;left:16px;top:481px;width:345px;height:99px;background:var(--comment);border-radius:8px;font-size:16px;color:var(--muted);padding:8px 0 0 12px}
.btn{position:absolute;top:607px;width:100px;height:40px;color:var(--white);font-size:25px;font-weight:500;text-align:center;line-height:40px;border-radius:3px}
.btn-next{left:260px;background:var(--navy)}
.btn-back{left:15px;background:var(--back)}
.btn-submit{left:247px;width:115px;background:var(--navy);border-radius:20px}
/* nav drawer */
.nav{background:var(--dim)}
.dim-panel{position:absolute;left:0;top:0;width:100%;height:472px;background:var(--dim-panel);border-radius:0 0 40px 40px}
.dim-box{position:absolute;left:17px;width:342px;height:46px;background:#6e6e6e;border-radius:8px}
.dim-comments{position:absolute;left:17px;top:489px;width:344px;height:100px;background:#878787;border-radius:8px;font-size:16px;color:#555;padding:10px 0 0 10px}
.dim-next{position:absolute;left:260px;top:607px;width:100px;height:40px;background:#1d3d6e;color:#8ea0b8;font-size:25px;font-weight:500;text-align:center;line-height:40px;border-radius:3px}
.drawer{position:absolute;left:0;top:0}
.avatar{position:absolute;left:21px;top:32px;width:50px;height:50px;border-radius:50%;background:linear-gradient(180deg,#f3d6b8,#e2593f);border:2px solid var(--white)}
.user-name{position:absolute;left:97px;top:34px;font-size:24px;color:var(--white)}
.user-phone{position:absolute;left:97px;top:63px;font-size:18px;color:#222}
.menu-item{position:absolute;left:22px;height:46px;display:flex;align-items:center;gap:29px;font-size:24px;font-weight:500;color:var(--white)}
.menu-item .icon{width:46px;height:46px;border-radius:50%;background:var(--white);display:flex;align-items:center;justify-content:center}
</style>
</head>
<body>
<div class="stage">
  <h1 class="page-title">SURVEY APP - MODEL 2</h1>

  <div class="screen-label" style="left:192px">SPLASH SCREEN</div>
  <div class="screen-label" style="left:666px">REGISTRATION</div>
  <div class="screen-label" style="left:1154px">NAV_BAR SCREEN</div>

  <!-- Splash -->
  <section class="screen splash" style="left:234px;top:341px">
    <div class="splash-brand"><span class="dot"></span><span>MERIDIAN NETWORKS</span></div>
  </section>

  <!-- Registration -->
  <section class="screen" style="left:714px;top:341px">
    <div class="header"></div>
    <div class="status"><span class="time">9:41</span>
      <svg width="80" height="18" viewBox="0 0 80 18" fill="#fff"><rect x="0" y="10" width="3" height="5"/><rect x="5" y="7" width="3" height="8"/><rect x="10" y="4" width="3" height="11"/><rect x="15" y="1" width="3" height="14"/><path d="M29 6a12 12 0 0 1 16 0l-2 2a9 9 0 0 0-12 0zM32 9a7 7 0 0 1 10 0l-2 2a4 4 0 0 0-6 0zM37 14l-2-2a3 3 0 0 1 4 0z"/><rect x="52" y="2" width="26" height="13" rx="3" fill="none" stroke="#fff" stroke-width="1.5"/><rect x="54" y="4" width="22" height="9" rx="1.5"/></svg>
    </div>
    <div class="reg-title">REGISTRATION</div>
    <div class="card"></div>
    <div class="field" style="top:184px">Name</div>
    <div class="field" style="top:264px">Phone Number</div>
    <div class="field" style="top:345px">Group Number</div>
    <p class="agree">By Registering I Agree To Participate In The Survey.</p>
    <div class="btn-register">REGISTER</div>
  </section>

  <!-- Nav drawer -->
  <section class="screen nav" style="left:1196px;top:341px">
    <div class="dim-panel"></div>
    <div class="dim-box" style="top:320px"></div>
    <div class="dim-box" style="top:391px"></div>
    <div class="dim-comments">Comments</div>
    <div class="dim-next">Next</div>
    <svg class="drawer" width="376" height="430" viewBox="0 0 376 430">
      <defs><linearGradient id="drawerFill" x1="1" y1="0" x2="0" y2="1"><stop offset="0" stop-color="#d3eefd"/><stop offset="1" stop-color="#4fb0f2"/></linearGradient></defs>
      <path d="M0 0H376V232C376 345 300 425 200 425H0Z" fill="url(#drawerFill)"/>
    </svg>
    <div class="avatar" role="img" aria-label="User profile avatar"></div>
    <div class="user-name">Name</div>
    <div class="user-phone">Phone Number</div>
    <div class="menu-item" style="top:114px"><span class="icon"><svg width="26" height="26" viewBox="0 0 26 26" fill="none" stroke="#4fb0f2" stroke-width="1.8"><circle cx="12" cy="8" r="5"/><path d="M3 24c0-6 4-9 9-9s7 2 8 4"/><path d="M17 23l6-6 2 2-6 6h-2z"/></svg></span>Edit User Profile</div>
    <div class="menu-item" style="top:168px"><span class="icon"><svg width="26" height="26" viewBox="0 0 26 26" fill="none" stroke="#4fb0f2" stroke-width="1.8"><rect x="5" y="3" width="16" height="21" rx="2"/><path d="M9 9h8M9 14h8M9 19h8"/></svg></span>Survey Interval Timer</div>
    <div class="menu-item" style="top:222px"><span class="icon"><svg width="26" height="26" viewBox="0 0 26 26" fill="none" stroke="#4fb0f2" stroke-width="1.8"><rect x="2" y="9" width="15" height="11" rx="2"/><path d="M5 13h9M5 16h6"/><circle cx="18" cy="7" r="5"/><path d="M16.5 6a1.5 1.5 0 1 1 2 1.4V9"/></svg></span>FAQ</div>
    <div class="menu-item" style="top:276px"><span class="icon"><svg width="26" height="26" viewBox="0 0 26 26" fill="none" stroke="#4fb0f2" stroke-width="1.8"><path d="M14 3h8v20h-8"/><path d="M3 13h13M12 9l4 4-4 4"/></svg></span>Exit</div>
    <div class="menu-item" style="top:330px"><span class="icon"><svg width="26" height="26" viewBox="0 0 26 26" fill="none" stroke="#4fb0f2" stroke-width="1.8"><circle cx="13" cy="13" r="10"/><path d="M13 11v7"/><circle cx="13" cy="8" r="0.8" fill="#4fb0f2"/></svg></span>About</div>
  </section>

  <div class="screen-label lower" style="left:9px">CALL EXPERIENCE</div>
  <div class="screen-label lower" style="left:460px">SMS EXPERIENCE</div>
  <div class="screen-label lower" style="left:917px">DATA EXPERIENCE</div>
  <div class="screen-label lower" style="left:1378px">STREAMING EXPERIENCE</div>

  <!-- Survey screens -->
  <section class="screen" style="left:51px;top:1232px">
    <div class="header"></div>
    <div class="status"><span class="time">9:41</span>
      <svg width="80" height="18" viewBox="0 0 80 18" fill="#fff"><rect x="0" y="10" width="3" height="5"/><rect x="5" y="7" width="3" height="8"/><rect x="10" y="4" width="3" height="11"/><rect x="15" y="1" width="3" height="14"/><path d="M29 6a12 12 0 0 1 16 0l-2 2a9 9 0 0 0-12 0zM32 9a7 7 0 0 1 10 0l-2 2a4 4 0 0 0-6 0zM37 14l-2-2a3 3 0 0 1 4 0z"/><rect x="52" y="2" width="26" height="13" rx="3" fill="none" stroke="#fff" stroke-width="1.5"/><rect x="54" y="4" width="22" height="9" rx="1.5"/></svg>
    </div>
    <svg class="burger" width="30" height="30" viewBox="0 0 30 30" stroke="#fff" stroke-width="4" stroke-linecap="round"><path d="M9 3h12M3 15h24M9 27h12"/></svg>
    <div class="survey-title">QUICK SURVEY</div>
    <div class="card"></div>
    <div class="feedback">Feedback</div>
    <div class="question"><h2>1. Call Experience</h2>
      <div class="option opt-1">Questionnaire or Satisfied</div>
      <div class="option opt-2">Somewhat Satisfied</div>
      <div class="option opt-3 selected">Extremely Satisfied</div>
    </div>
    <div class="comments">Comments</div>
    <div class="btn btn-next">Next</div>
  </section>

  <section class="screen" style="left:502px;top:1232px">
    <div class="header"></div>
    <div class="status"><span class="time">9:41</span>
      <svg width="80" height="18" viewBox="0 0 80 18" fill="#fff"><rect x="0" y="10" width="3" height="5"/><rect x="5" y="7" width="3" height="8"/><rect x="10" y="4" width="3" height="11"/><rect x="15" y="1" width="3" height="14"/><path d="M29 6a12 12 0 0 1 16 0l-2 2a9 9 0 0 0-12 0zM32 9a7 7 0 0 1 10 0l-2 2a4 4 0 0 0-6 0zM37 14l-2-2a3 3 0 0 1 4 0z"/><rect x="52" y="2" width="26" height="13" rx="3" fill="none" stroke="#fff" stroke-width="1.5"/><rect x="54" y="4" width="22" height="9" rx="1.5"/></svg>
    </div>
    <svg class="burger" width="30" height="30" viewBox="0 0 30 30" stroke="#fff" stroke-width="4" stroke-linecap="round"><path d="M9 3h12M3 15h24M9 27h12"/></svg>
    <div class="survey-title">QUICK SURVEY</div>
    <div class="card"></div>
    <div class="feedback">Feedback</div>
    <div class="question"><h2>2. SMS Experience</h2>
      <div class="option opt-1">Questionnaire or Satisfied</div>
      <div class="option opt-2">Somewhat Satisfied</div>
      <div class="option opt-3 selected">Extremely Satisfied</div>
    </div>
    <div class="comments">Comments</div>
    <div class="btn btn-back">Back</div>
    <div class="btn btn-next">Next</div>
  </section>

  <section class="screen" style="left:955px;top:1232px">
    <div class="header"></div>
    <div class="status"><span class="time">9:41</span>
      <svg width="80" height="18" viewBox="0 0 80 18" fill="#fff"><rect x="0" y="10" width="3" height="5"/><rect x="5" y="7" width="3" height="8"/><rect x="10" y="4" width="3" height="11"/><rect x="15" y="1" width="3" height="14"/><path d="M29 6a12 12 0 0 1 16 0l-2 2a9 9 0 0 0-12 0zM32 9a7 7 0 0 1 10 0l-2 2a4 4 0 0 0-6 0zM37 14l-2-2a3 3 0 0 1 4 0z"/><rect x="52" y="2" width="26" height="13" rx="3" fill="none" stroke="#fff" stroke-width="1.5"/><rect x="54" y="4" width="22" height="9" rx="1.5"/></svg>
    </div>
    <svg class="burger" width="30" height="30" viewBox="0 0 30 30" stroke="#fff" stroke-width="4" stroke-linecap="round"><path d="M9 3h12M3 15h24M9 27h12"/></svg>
    <div class="survey-title">QUICK SURVEY</div>
    <div class="card"></div>
    <div class="feedback">Feedback</div>
    <div class="question"><h2>3. Data Experience</h2>
      <div class="option opt-1">Questionnaire or Satisfied</div>
      <div class="option opt-2 selected">Somewhat Satisfied</div>
      <div class="option opt-3">Extremely Satisfied</div>
    </div>
    <div class="comments">Comments</div>
    <div class="btn btn-back">Back</div>
    <div class="btn btn-next">Next</div>
  </section>

  <section class="screen" style="left:1413px;top:1232px">
    <div class="header"></div>
    <div class="status"><span class="time">9:41</span>
      <svg width="80" height="18" viewBox="0 0 80 18" fill="#fff"><rect x="0" y="10" width="3" height="5"/><rect x="5" y="7" width="3" height="8"/><rect x="10" y="4" width="3" height="11"/><rect x="15" y="1" width="3" height="14"/><path d="M29 6a12 12 0 0 1 16 0l-2 2a9 9 0 0 0-12 0zM32 9a7 7 0 0 1 10 0l-2 2a4 4 0 0 0-6 0zM37 14l-2-2a3 3 0 0 1 4 0z"/><rect x="52" y="2" width="26" height="13" rx="3" fill="none" stroke="#fff" stroke-width="1.5"/><rect x="54" y="4" width="22" height="9" rx="1.5"/></svg>
    </div>
    <svg class="burger" width="30" height="30" viewBox="0 0 30 30" stroke="#fff" stroke-width="4" stroke-linecap="round"><path d="M9 3h12M3 15h24M9 27h12"/></svg>
    <div class="survey-title">QUICK SURVEY</div>
    <div class="card"></div>
    <div class="feedback">Feedback</div>
    <div class="question"><h2>4. Streaming Experience</h2>
      <div class="option opt-1">Questionnaire or Satisfied</div>
      <div class="option opt-2">Somewhat Satisfied</div>
      <div class="option opt-3 selected">Extremely Satisfied</div>
    </div>
    <div class="comments">Comments</div>
    <div class="btn btn-back">Back</div>
    <div class="btn btn-submit">SUBMIT</div>
  </section>
</div>
</body>
</html>
```